Veltora Software Business Card Design

We are a new organization called Veltora. We are a software as a service provider. We deliver a project and program management solution via the internet, so everyone has the ability to work together and collaborate. Its an enterprise platform and we will focus on 50 plus employee company.

We have a website in place
www.veltora-demo.com

Use this as a start of producing the business card. The logo is there as well, but if you have a great and better solution...

Color scheme's could be inline with the website, but don't pin point on it. We can always change the website, logo, color scheme etc.

Target Market(s)

B2B, Projectmembers, projectmanagers, ICT, CTO, Marketing Managers

Industry/Entity Type

Software

Requirements
Must have
• Marten Kuyvelsma

Tel: +31 255 47 09 36
Mob: +31 6 927 15 062
marten@veltora-demo.com
Oostelingpad 84c
2184 KT Nieuw Vennep

Www.veltora-demo.com
social media links

```html
<!DOCTYPE html>
<html lang="en">
<head>
<meta charset="utf-8">
<title>Veltora Software Business Card Design</title>
<link rel="stylesheet" href="https://fonts.googleapis.com/css2?family=Michroma&family=Open+Sans:wght@300;400&display=swap">
<style>
  :root {
    --page: #ececec;
    --olive: #8d991f;
    --olive-soft: #9aa72a;
    --olive-deep: #6f7a14;
    --olive-dark: #4a5010;
    --lime: #b9c816;
    --ink: #111111;
    --text-grey: #555555;
    --white: #ffffff;
  }
  * { margin: 0; padding: 0; box-sizing: border-box; }
  html, body {
    width: 1200px;
    height: 848px;
    overflow: hidden;
    background: var(--page);
  }
  .sheet { position: relative; width: 1200px; height: 848px; }
  .card {
    position: absolute;
    width: 560px;
    height: 338px;
    overflow: hidden;
    box-shadow: 0 3px 6px rgba(0, 0, 0, 0.35);
  }
  .card svg { display: block; width: 100%; height: 100%; }
  .card--contact { left: 100px; top: 326px; background: var(--olive); }
  .card--brand { left: 544px; top: 137px; background: var(--white); }

  .holder-name {
    font-family: "Michroma", sans-serif;
    font-size: 19px;
    letter-spacing: 2px;
    fill: var(--white);
  }
  .contact-line {
    font-family: "Open Sans", sans-serif;
    font-size: 14px;
    fill: var(--text-grey);
  }
  .contact-line--mail { letter-spacing: 0.6px; }
  .address-line {
    font-family: "Open Sans", sans-serif;
    font-size: 12.5px;
    fill: var(--white);
  }
  .web-line {
    font-family: "Open Sans", sans-serif;
    font-size: 12.5px;
    letter-spacing: 2.4px;
    fill: var(--white);
  }
  .social-line {
    font-family: "Open Sans", sans-serif;
    font-size: 11px;
    letter-spacing: 1px;
    fill: var(--white);
  }
  .brand-name {
    font-family: "Open Sans", sans-serif;
    font-weight: 300;
    font-size: 44px;
    fill: var(--ink);
  }
</style>
</head>
<body>
<main class="sheet">

  <section class="card card--contact" aria-label="Contact side">
    <svg viewBox="0 0 546 328" preserveAspectRatio="none">
      <defs>
        <linearGradient id="contact-art-fill" x1="0" y1="0" x2="1" y2="1">
          <stop offset="0" stop-color="#7c8b22"/>
          <stop offset="0.6" stop-color="var(--olive-soft)"/>
          <stop offset="1" stop-color="var(--olive)"/>
        </linearGradient>
        <linearGradient id="contact-art-fade" x1="0" y1="0" x2="0" y2="1">
          <stop offset="0" stop-color="#ffffff" stop-opacity="1"/>
          <stop offset="0.75" stop-color="#ffffff" stop-opacity="1"/>
          <stop offset="1" stop-color="#ffffff" stop-opacity="0"/>
        </linearGradient>
        <mask id="contact-art-mask">
          <rect width="546" height="230" fill="url(#contact-art-fade)"/>
        </mask>
      </defs>
      <rect class="base" width="546" height="328" fill="var(--olive)"/>
      <rect class="ribbon-art" width="546" height="230" fill="url(#contact-art-fill)" mask="url(#contact-art-mask)"
            role="img" aria-label="Faint folded ribbon illustration in olive tones"/>

      <text class="holder-name" x="37" y="149">MARTEN KUYVELSMA</text>

      <path class="contact-box" d="M0,163 H296 A6,6 0 0 1 302,169 V234 A6,6 0 0 1 296,240 H0 Z" fill="var(--white)"/>
      <text class="contact-line" x="38" y="185">Tel:  +31 255 47 09 36</text>
      <text class="contact-line" x="38" y="207">Mob:  +31 6 927 15 062</text>
      <text class="contact-line contact-line--mail" x="38" y="229">marten@veltora-demo.com</text>

      <text class="address-line" x="318" y="192">Oostelingpad 84c</text>
      <text class="address-line" x="318" y="206">2184 KT Nieuw Vennep</text>
      <text class="web-line" x="318" y="229">WWW.VELTORA-DEMO.COM</text>
      <text class="social-line" x="318" y="252">Social: @veltora</text>
    </svg>
  </section>

  <section class="card card--brand" aria-label="Brand side">
    <svg viewBox="0 0 546 330" preserveAspectRatio="none">
      <defs>
        <linearGradient id="brand-art-fill" x1="0" y1="1" x2="1" y2="0">
          <stop offset="0" stop-color="var(--olive-dark)"/>
          <stop offset="0.45" stop-color="var(--olive-deep)"/>
          <stop offset="1" stop-color="var(--lime)"/>
        </linearGradient>
      </defs>
      <rect class="base" width="546" height="330" fill="var(--white)"/>
      <polygon class="ribbon-art" points="0,100 200,100 330,0 546,0 546,180 300,180 300,210 0,310"
               fill="url(#brand-art-fill)"
               role="img" aria-label="Folded ribbon illustration in olive and lime green"/>

      <text class="brand-name" x="312" y="272">Veltora</text>
    </svg>
  </section>

</main>
</body>
</html>
```